Z-Reel Carnival Podcast Cover Design

We need a podcast cover (square design) for a podcast called Z-Reel Carnival.
MANDATORY: Z-REEL CARNIVAL
OPTIONAL: with The Creature Nerd Dale Furnow

Z-Reel Carnival is a movie podcast dedicated to covering all of the cult oddities you saw in theaters and video stores as a kid but never got to rent or watch. Focusing on obscure horror, cult oddities, action movies, exploitation movies, foreign knockoffs, and more, this a show designed to help you take a trip down memory lane or find new weird movies to add to your streaming queue. Come take a walk on the wild side of cinema at Z-Reel Carnival,..where one person's trash movie is our treasure.
##
Fonts that fit the vibe we're going for:
https://www.typevault.example/sets/grindhouse-drip-font-kelvorn-studio
https://www.pinboardly.example/pin/481926035517204963/
https://www.typevault.example/sets/grindhouse-vintage-font-kelvorn-studio

Target Market(s)

Primarily male, although we have some female fans as well. Podcast fans of B-movies (inexpensively made and a bit outrageous), cult movies, weird movies, old movies, horror movies, and action films.

Industry/Entity Type

Media - Movies -Podcast

Font styles to use
Other font styles liked:
• Fonts that fit the vibe: Fonts: https://www.typevault.example/sets/grindhouse-drip-font-kelvorn-studio https://www.pinboardly.example/pin/481926035517204963/ https://www.typevault.example/sets/grindhouse-vintage-font-kelvorn-studio

Colors
EB3D1F
EC4F4E
F09395
F8D3D4
FCEDEE

Requirements
Must have
• Z-REEL CARNIVAL
Nice to have
• 1) with The Creature Nerd Dale Furnow; 2) VISUALS: VHS tapes

```html
<!DOCTYPE html>
<html lang="en">
<head>
<meta charset="utf-8">
<title>Z-Reel Carnival — Podcast Cover</title>
<link rel="stylesheet" href="https://fonts.googleapis.com/css2?family=Rubik+Dirt&family=Montserrat:wght@600;700&display=swap">
<style>
  :root {
    --stage: #2b2829;
    --cover: #2f2e2e;
    --cover-deep: #1f1e1e;
    --cover-edge: #9a9898;
    --title-red: #e3213f;
    --credit-grey: #8d8b8b;
  }
  * { margin: 0; padding: 0; box-sizing: border-box; }
  html, body {
    width: 1200px;
    height: 807px;
    overflow: hidden;
    background: var(--stage);
  }
  .stage {
    position: relative;
    width: 1200px;
    height: 807px;
  }
  .podcast-cover {
    position: absolute;
    left: 290px;
    top: 93px;
    width: 620px;
    height: 620px;
    background: var(--cover);
    border: 2px solid var(--cover-edge);
    outline: 1px solid rgba(0,0,0,0.5);
    overflow: hidden;
  }
  .cover-atmosphere {
    position: absolute;
    inset: 0;
    background:
      radial-gradient(ellipse 38% 46% at 50% 48%, rgba(20,19,19,0.75), rgba(20,19,19,0) 70%),
      radial-gradient(ellipse 22% 30% at 12% 18%, rgba(18,17,17,0.55), rgba(18,17,17,0) 70%),
      radial-gradient(ellipse 22% 30% at 88% 18%, rgba(18,17,17,0.55), rgba(18,17,17,0) 70%),
      radial-gradient(ellipse 26% 30% at 22% 78%, rgba(18,17,17,0.45), rgba(18,17,17,0) 70%),
      radial-gradient(ellipse 26% 30% at 80% 70%, rgba(18,17,17,0.45), rgba(18,17,17,0) 70%),
      linear-gradient(180deg, #333232 0%, var(--cover) 50%, #2a2929 100%);
  }
  .podcast-title {
    position: absolute;
    left: 40px;
    right: 40px;
    top: 170px;
    text-align: center;
    font-family: "Rubik Dirt", "Impact", sans-serif;
    font-weight: 400;
    font-size: 88px;
    line-height: 94px;
    letter-spacing: 1px;
    white-space: nowrap;
    color: var(--title-red);
    transform: rotate(-1deg) scaleY(1.25);
    transform-origin: 50% 50%;
  }
  .podcast-title span { display: block; }
  .podcast-credit {
    position: absolute;
    left: 0;
    right: 0;
    bottom: 22px;
    text-align: center;
    font-family: "Montserrat", "Helvetica", sans-serif;
    font-weight: 700;
    font-size: 19px;
    line-height: 23px;
    color: var(--credit-grey);
    letter-spacing: 0.4px;
  }
  .podcast-credit span { display: block; }
</style>
</head>
<body>
  <main class="stage">
    <section class="podcast-cover">
      <div class="cover-atmosphere" role="img" aria-label="Grainy dark photo of shadowy hands pressed against frosted glass"></div>
      <h1 class="podcast-title"><span>Z-REEL</span><span>CARNIVAL</span></h1>
      <p class="podcast-credit"><span>with The Creature Nerd</span><span>DALE FURNOW</span></p>
    </section>
  </main>
</body>
</html>
```